DWR Logistics Marketing flyer

Good morning, I run a trucking company and I will be needing help setting up a website logo and a marketing flyer or something like that talking about our services and what we can offer to potential new customers who need to ship their product. I need help getting this all together.

Target Market(s)

Transportation customers

Requirements
Must have
• should list our services and contact info
Nice to have
• the Logo on the top

```html
<!DOCTYPE html>
<html lang="en">
<head>
<meta charset="utf-8">
<title>DWR Logistics – Logistic and Transport</title>
<link rel="stylesheet" href="https://fonts.googleapis.com/css2?family=Montserrat:wght@600;700&family=Roboto:wght@500;700&display=swap">
<style>
  :root{
    --navy:#141a33;
    --navy-deep:#0f1428;
    --crimson:#c8405a;
    --crimson-dark:#8e2338;
    --rose:#d9475f;
    --white:#ffffff;
  }
  *{margin:0;padding:0;box-sizing:border-box}
  html,body{width:848px;height:1200px;overflow:hidden;background:var(--navy)}
  .flyer{position:relative;width:848px;height:1200px;overflow:hidden;
    background:radial-gradient(ellipse at 50% 60%,#1b2242 0%,var(--navy) 55%,var(--navy-deep) 100%);
    font-family:"Montserrat",sans-serif;color:var(--white)}
  .hero-photo{position:absolute;left:0;top:0;width:848px;height:490px;
    background:linear-gradient(90deg,#151b35 0%,#2a3040 14%,#5d6a4c 28%,#7b2c3f 38%,#9aa3a6 52%,#d9dde2 70%,#eef0f3 100%)}
  .hero-rule{position:absolute;left:0;top:490px;width:848px;height:4px;background:var(--white)}
  .band{position:absolute;height:11px}
  .band-top{left:0;top:496px;width:848px;background:linear-gradient(90deg,var(--crimson) 0%,#7a2a44 45%,#7a2a44 55%,var(--crimson) 100%)}
  .band-second{left:0;top:528px;width:848px;background:linear-gradient(90deg,var(--crimson) 0%,rgba(200,64,90,0) 40%,rgba(200,64,90,0) 60%,var(--crimson) 100%)}
  .logo-badge{position:absolute;left:34px;top:0;width:199px;height:152px}
  .logo-badge svg{position:absolute;inset:0}
  .logo-name{position:absolute;left:0;top:44px;width:199px;text-align:center;
    font-family:"Roboto",sans-serif;font-weight:700;font-size:30px;line-height:34px;letter-spacing:1px;color:var(--white)}
  .logo-name span{display:block;font-size:13px;line-height:18px;letter-spacing:3px}
  .logo-est{position:absolute;left:0;top:126px;width:199px;text-align:center;
    font-family:"Roboto",sans-serif;font-weight:500;font-size:9px;color:var(--white)}
  .kicker{position:absolute;left:0;top:537px;width:848px;text-align:center;
    font-weight:700;font-size:24px;letter-spacing:9px;color:var(--rose)}
  .headline{position:absolute;left:0;top:586px;width:848px;text-align:center;
    font-family:"Roboto",sans-serif;font-weight:500;font-size:70px;line-height:76px;letter-spacing:4px}
  .deco-arrows{position:absolute;left:26px;top:702px}
  .deco-dots{position:absolute;left:700px;top:694px}
  .service-ribbon{position:absolute;left:196px;top:768px;width:456px;height:59px}
  .service-ribbon svg{position:absolute;inset:0}
  .service-ribbon p{position:absolute;inset:0;display:flex;align-items:center;justify-content:center;
    font-weight:600;font-size:25px;letter-spacing:8px}
  .service-photo{position:absolute;top:867px;width:184px;height:184px;border-radius:50%;border:2px solid var(--white)}
  .photo-containers{left:73px;background:linear-gradient(180deg,#5aa8e6 0%,#c8563f 45%,#2e5a8a 75%,#c9c0a8 100%)}
  .photo-loading{left:331px;background:linear-gradient(135deg,#3a3028 0%,#c79a6a 45%,#9c9aa0 75%,#b47a48 100%)}
  .photo-parcel{left:590px;background:linear-gradient(135deg,#e7e9ea 0%,#d83a3a 40%,#c8995e 70%,#f0f0f0 100%)}
  .phone{position:absolute;left:0;top:1078px;width:848px;text-align:center;
    font-family:"Roboto",sans-serif;font-weight:700;font-size:56px;line-height:68px}
  .side-bar{position:absolute;top:1129px;height:13px;width:159px}
  .side-bar.left{left:0;background:linear-gradient(90deg,var(--crimson),#3b2440)}
  .side-bar.right{right:0;background:linear-gradient(90deg,#3b2440,var(--crimson))}
  .footer-band{position:absolute;top:1161px;height:12px}
  .footer-band.left{left:0;width:295px;background:linear-gradient(90deg,var(--crimson),#4a2744)}
  .footer-band.right{left:558px;width:290px;background:linear-gradient(90deg,#4a2744,var(--crimson))}
  .website{position:absolute;left:0;top:1158px;width:848px;text-align:center;
    font-family:"Roboto",sans-serif;font-weight:500;font-size:13px;line-height:18px}
</style>
</head>
<body>
<main class="flyer">
  <div class="hero-photo" role="img" aria-label="Smiling delivery driver giving thumbs up beside a white delivery van"></div>
  <div class="hero-rule"></div>
  <div class="band band-top"></div>
  <div class="band band-second"></div>

  <div class="logo-badge">
    <svg width="199" height="152" viewBox="0 0 199 152">
      <defs><linearGradient id="badgeFill" x1="0" y1="0" x2="0" y2="1">
        <stop offset="0" stop-color="#d04861"/><stop offset="1" stop-color="#a42f47"/></linearGradient></defs>
      <polygon points="0,0 199,0 199,134 100,152 0,134" fill="url(#badgeFill)"/>
    </svg>
    <div class="logo-name">DWR<span>LOGISTICS LLC</span></div>
    <div class="logo-est">EST. 2010</div>
  </div>

  <p class="kicker">FAST AND EFFICIENT</p>
  <h1 class="headline">LOGISTIC AND<br>TRANSPORT</h1>

  <svg class="deco-arrows" width="112" height="12" viewBox="0 0 112 12" fill="#fff">
    <polygon points="0,0 9,6 0,12"/><polygon points="24,0 33,6 24,12"/>
    <polygon points="48,0 57,6 48,12"/><polygon points="100,0 109,6 100,12"/>
  </svg>
  <svg class="deco-dots" width="140" height="42" viewBox="0 0 140 42" fill="#fff">
    <circle cx="26" cy="5" r="2.5"/><circle cx="60" cy="5" r="2.5"/><circle cx="93" cy="5" r="2.5"/><circle cx="127" cy="5" r="2.5"/>
    <circle cx="6" cy="22" r="2.5"/><circle cx="40" cy="22" r="2.5"/><circle cx="73" cy="22" r="2.5"/><circle cx="107" cy="22" r="2.5"/><circle cx="138" cy="22" r="2.5"/>
    <circle cx="26" cy="39" r="2.5"/><circle cx="60" cy="39" r="2.5"/><circle cx="93" cy="39" r="2.5"/><circle cx="127" cy="39" r="2.5"/>
  </svg>

  <div class="service-ribbon">
    <svg width="456" height="59" viewBox="0 0 456 59">
      <defs><linearGradient id="ribbonFill" x1="0" y1="0" x2="0" y2="1">
        <stop offset="0" stop-color="#d04861"/><stop offset="1" stop-color="#962a40"/></linearGradient></defs>
      <polygon points="18,0 438,0 456,29.5 438,59 18,59 0,29.5" fill="url(#ribbonFill)"/>
    </svg>
    <p>THE BEST SERVICE</p>
  </div>

  <div class="service-photo photo-containers" role="img" aria-label="Stacked shipping containers at a cargo port"></div>
  <div class="service-photo photo-loading" role="img" aria-label="Woman checking a tablet beside a van loaded with boxes"></div>
  <div class="service-photo photo-parcel" role="img" aria-label="Courier in red cap carrying a parcel from a delivery van"></div>

  <p class="phone">555-214-7360</p>
  <div class="side-bar left"></div>
  <div class="side-bar right"></div>

  <div class="footer-band left"></div>
  <div class="footer-band right"></div>
  <p class="website">WWW.DWRLOGISTICSLLC.COM</p>
</main>
</body>
</html>
```